2nd Generation Blind Manufacturer & Retailer Needs A Stationary Set

We need a stationary set for a family business located the in the Whitsundays (QLD). We retail and manufacture blinds awnings and shutters. Second generation, in operation for over 30 years.

Final draft must include at minimum:

Business Card (2 Sided)
Letterhead
Presentation Folder

Target Market(s)

home owners, landlords, builders, real estate agents, shopping centres

Industry/Entity Type

Textile

Requirements
Must have
• Design needs to work in mono as well as colour print
Nice to have
• Relevant to the textile industry
Should not have
• The inclusion of blinds, awnings or shutters is an automatic no-no

```html
<!DOCTYPE html>
<html lang="en">
<head>
<meta charset="utf-8">
<title>Harlow Blinds – Business Card</title>
<link rel="stylesheet" href="https://fonts.googleapis.com/css2?family=Montserrat:wght@400;600;700&display=swap">
<style>
  :root {
    --backdrop: #dcdcee;
    --card-white: #f4f5f7;
    --card-grey: #6a6c6e;
    --ink-dark: #4a4c4f;
    --ink-mid: #66686b;
    --band-light: #a8a9ad;
    --band-dark: #626467;
    --paper-text: #ffffff;
  }
  * { margin: 0; padding: 0; box-sizing: border-box; }
  html, body {
    width: 1200px; height: 906px; overflow: hidden;
    background: var(--backdrop);
    font-family: "Montserrat", sans-serif;
  }
  .canvas { position: relative; width: 1200px; height: 906px; }

  .card {
    position: absolute;
    width: 500px; height: 286px;
    box-shadow: 0 6px 18px rgba(60, 60, 100, 0.18);
  }

  /* Back side */
  .card-back { left: 80px; top: 130px; background: var(--card-grey); color: var(--paper-text); }
  .card-back .brand {
    position: absolute; left: 0; right: 0; top: 104px;
    display: flex; align-items: center; justify-content: center; gap: 14px;
  }
  .card-back .brand-square { width: 34px; height: 34px; background: var(--paper-text); }
  .card-back .brand-name { font-weight: 600; font-size: 30px; letter-spacing: 3px; text-transform: uppercase; }
  .card-back .web {
    position: absolute; left: 0; right: 0; top: 190px;
    text-align: center; font-size: 12px; letter-spacing: 1px;
  }

  /* Front side */
  .card-front { left: 620px; top: 470px; background: var(--card-white); color: var(--ink-dark); }
  .card-front .brand {
    position: absolute; right: 40px; top: 48px;
    display: flex; align-items: center; gap: 10px;
  }
  .card-front .brand-square { width: 26px; height: 26px; background: var(--ink-mid); }
  .card-front .brand-name { font-weight: 600; font-size: 22px; letter-spacing: 2px; text-transform: uppercase; color: var(--ink-mid); }

  .holder { position: absolute; left: 42px; top: 126px; }
  .holder-name { font-weight: 700; font-size: 17px; letter-spacing: 0.5px; text-transform: uppercase; }
  .holder-title { font-size: 12px; color: var(--ink-mid); margin-top: 2px; }

  .address {
    position: absolute; right: 40px; top: 132px;
    text-align: right; font-size: 11.5px; line-height: 16px; color: var(--ink-dark);
  }

  .contacts { position: absolute; left: 42px; top: 164px; list-style: none; font-size: 11.5px; }
  .contacts li { display: flex; align-items: center; gap: 8px; height: 17px; }
  .contacts svg { width: 13px; height: 13px; flex: none; }

  .rule-thin { position: absolute; left: 16px; right: 16px; top: 232px; height: 3px; background: var(--band-light); }
  .rule-thick { position: absolute; left: 16px; right: 16px; top: 243px; height: 18px; background: var(--band-dark); }
</style>
</head>
<body>
<main class="canvas">

  <section class="card card-back" aria-label="Business card, back">
    <div class="brand">
      <span class="brand-square"></span>
      <span class="brand-name">Harlow Blinds</span>
    </div>
    <p class="web">www.harlowblinds.com</p>
  </section>

  <section class="card card-front" aria-label="Business card, front">
    <div class="brand">
      <span class="brand-square"></span>
      <span class="brand-name">Harlow Blinds</span>
    </div>

    <div class="holder">
      <p class="holder-name">Daniel Reeve</p>
      <p class="holder-title">General Manager</p>
    </div>

    <p class="address">118 Marina Parade<br>Airlie Beach, QLD 4802</p>

    <ul class="contacts">
      <li>
        <svg viewBox="0 0 14 14" aria-hidden="true"><rect width="14" height="14" rx="2" fill="#4a4c4f"/><path d="M4 3.2l1.6 0 .6 2-1 .8c.5 1.2 1.5 2.2 2.7 2.7l.8-1 2 .6v1.6c-4 .3-7-2.7-6.7-6.7z" fill="#fff"/></svg>
        <span>555.014.2300</span>
      </li>
      <li>
        <svg viewBox="0 0 14 14" aria-hidden="true"><rect width="14" height="14" rx="2" fill="#4a4c4f"/><rect x="4" y="2.5" width="6" height="3" fill="#fff"/><rect x="2.5" y="6" width="9" height="4" fill="#fff"/><rect x="4" y="9" width="6" height="2.5" fill="#fff"/></svg>
        <span>555.014.2400</span>
      </li>
      <li>
        <svg viewBox="0 0 14 14" aria-hidden="true"><rect width="14" height="14" rx="2" fill="#4a4c4f"/><circle cx="7" cy="7" r="4.3" fill="none" stroke="#fff" stroke-width="1"/><ellipse cx="7" cy="7" rx="1.8" ry="4.3" fill="none" stroke="#fff" stroke-width="0.8"/><path d="M2.7 7h8.6" stroke="#fff" stroke-width="0.8"/></svg>
        <span>www.harlowblinds.com</span>
      </li>
    </ul>

    <div class="rule-thin"></div>
    <div class="rule-thick"></div>
  </section>

</main>
</body>
</html>
```